Software Company Business Card

We are looking for a new design of our business card. The design will also be used in the rest of our branding and marketing materials as we want to keep it all uniform. We sell POS software to fine/luxury jewelers and also offer other business services as well to help the jeweler manage their business and need something more updated, technical and fresh, preferably more on the masculine side. We do not want any designs with gems in them but if possible would like to incorporate the circle and arrow in the logo into the design, but not a requirement if you can't make it work. I would like to see a variety of the mix. The colors need to remain our blue and orange and the logo can not change. The squiggly lines have been used as our corporate identity for over 20 years and its time to update. Our company name is PELK (Bright Ledger Counter Solutions).

Target Market(s)

High End Jewelers

Industry/Entity Type

Software

Contact Information for Business Card

Requirements
Must have
• Our logo and the colors must remain the same. Blue is #d95d39 and Orange is #0f5682.
Nice to have
• The circle and arrow incorporated but not a requirement.
Should not have
• Anything jewelry or gem related.

```html
<!DOCTYPE html>
<html lang="en">
<head>
<meta charset="utf-8">
<title>PELK Business Card</title>
<link rel="stylesheet" href="https://fonts.googleapis.com/css2?family=Montserrat:wght@400;500;700&display=swap">
<style>
  :root {
    --blue: #03568a;
    --orange: #d95d39;
    --ink: #555a5e;
    --paper: #ffffff;
    --backdrop: #d9d9d9;
  }
  * { margin: 0; padding: 0; box-sizing: border-box; }
  html, body { width: 1200px; height: 1200px; overflow: hidden; }
  body {
    background: var(--backdrop);
    font-family: "Montserrat", Arial, sans-serif;
    position: relative;
  }
  .card {
    position: absolute;
    left: 211px;
    width: 738px;
    height: 422px;
    overflow: hidden;
  }
  .card-front { top: 111px; background: var(--paper); }
  .card-back { top: 626px; background: var(--orange); }

  .brand {
    position: absolute;
    display: flex;
    align-items: center;
  }
  .brand-name {
    font-weight: 700;
    color: var(--blue);
    line-height: 1;
    letter-spacing: -0.02em;
  }
  .brand-dot { border-radius: 50%; flex: none; }

  .card-front .brand { left: 47px; top: 180px; gap: 14px; }
  .card-front .brand-name { font-size: 60px; }
  .card-front .brand-dot { width: 64px; height: 64px; background: var(--orange); }

  .card-back .brand { left: 122px; top: 160px; gap: 22px; }
  .card-back .brand-name { font-size: 104px; }
  .card-back .brand-dot { width: 104px; height: 104px; background: var(--paper); }

  .divider {
    position: absolute;
    left: 380px; top: 87px;
    width: 1.5px; height: 252px;
    background: var(--orange);
  }
  .details {
    position: absolute;
    left: 411px; top: 78px;
    color: var(--ink);
  }
  .person-name {
    font-size: 29px;
    font-weight: 500;
    color: var(--blue);
    line-height: 1.1;
    letter-spacing: 0.01em;
  }
  .person-title { font-size: 17.5px; margin-top: 1px; letter-spacing: 0.02em; }
  .address { font-size: 18px; line-height: 23.5px; margin-top: 14px; letter-spacing: 0.03em; }
  .contacts { list-style: none; margin-top: 9px; }
  .contacts li {
    display: flex; align-items: center; gap: 8px;
    font-size: 18px; line-height: 24px; letter-spacing: 0.03em;
  }
  .contacts svg { width: 14px; height: 14px; flex: none; }
  .site-name { color: var(--blue); font-weight: 700; }

  .footer-band {
    position: absolute; left: 0; bottom: 0;
    width: 100%; height: 12px; display: flex;
  }
  .footer-band span { flex: 1; }
  .band-blue { background: var(--blue); }
  .band-orange { background: var(--orange); }
</style>
</head>
<body>
  <section class="card card-front">
    <div class="brand">
      <span class="brand-name">PELK</span>
      <span class="brand-dot"></span>
    </div>
    <div class="divider"></div>
    <div class="details">
      <h1 class="person-name">Dorian Whitcombe</h1>
      <p class="person-title">Director of Global Operations</p>
      <p class="address">1480 Meridian Parkway<br>Suite 210<br>Carson City, NV 89706<br>USA</p>
      <ul class="contacts">
        <li>
          <svg viewBox="0 0 16 16" aria-hidden="true"><path d="M4 1.5l2.2 3-1.3 1.3c.6 1.8 2 3.5 3.8 4.6l1.3-1.3 3 2.2-1.5 2.4C7 13 3 8.5 2.3 3.2z" fill="none" stroke="#d95d39" stroke-width="1.4" stroke-linejoin="round"/></svg>
          <span>+1 555 014-2287</span>
        </li>
        <li>
          <svg viewBox="0 0 16 16" aria-hidden="true"><rect x="4" y="1.5" width="8" height="4" fill="#d95d39"/><rect x="1" y="5.5" width="14" height="6" rx="1.5" fill="#d95d39"/><rect x="4" y="9.5" width="8" height="5" fill="#d95d39" stroke="#fff" stroke-width="1"/></svg>
          <span>+1 555 017-3940</span>
        </li>
        <li>
          <svg viewBox="0 0 16 16" aria-hidden="true"><rect x="1.5" y="3.5" width="13" height="9" fill="none" stroke="#d95d39" stroke-width="1.4"/><path d="M1.5 3.5L8 9l6.5-5.5" fill="none" stroke="#d95d39" stroke-width="1.4"/></svg>
          <span>dorian@pelkledger.com</span>
        </li>
        <li>
          <svg viewBox="0 0 16 16" aria-hidden="true"><g fill="none" stroke="#d95d39" stroke-width="1.1"><circle cx="8" cy="8" r="6.5"/><ellipse cx="8" cy="8" rx="3" ry="6.5"/><path d="M1.5 8h13M2.5 4.8h11M2.5 11.2h11"/></g></svg>
          <span>www.<span class="site-name">pelkledger</span>.com</span>
        </li>
      </ul>
    </div>
    <div class="footer-band"><span class="band-blue"></span><span class="band-orange"></span></div>
  </section>

  <section class="card card-back">
    <div class="brand">
      <span class="brand-name">PELK</span>
      <span class="brand-dot"></span>
    </div>
  </section>
</body>
</html>
```